Seller Looking for a luxurious diverse ethnic look...stunning but not overly seductive

I need a web Design for a company based in NEW YORK CITY called Velvet Harbor LLC. Initially I will be selling clothing and accessories as well as electronics on Tradora and hope to branch out. I want the whole experience for my customers and people I will buy from when they deal with me to be confident that this will be a velvet harbor and luxurious transaction.
Updates

Project Deadline Extended Reason: As I keep getting these great designs I continue to get more ideas and feel more time will help get us there. Added Thursday, July 16, 2015

Target Market(s)

ages 20-60

Industry/Entity Type

Clothing

Number of Pages Required

1 page

Font styles to use
Script

Colors
b768aa

Requirements
Must have
• Sleek and Luxurious feel and modern. I would like the page to look startling stunning yet not overly seductive and to include ethnic diversity. I like the illusion not knowing what the sight is selling since I am not targeting one area.
Should not have
• Do not want it to look generic or traditional

```html
<!DOCTYPE html>
<html lang="en">
<head>
<meta charset="utf-8">
<title>Velvet Harbor</title>
<link rel="stylesheet" href="https://fonts.googleapis.com/css2?family=Pacifico&family=Montserrat:wght@400;600;700&family=Raleway:wght@300;400;600&display=swap">
<style>
:root{
  --ink:#1c1c1c;
  --dark:#262626;
  --darker:#1a1a1a;
  --white:#ffffff;
  --gray-band:#dcdcdc;
  --muted:#8a8a8a;
  --green:#1fa34a;
  --plum:#7b3a82;
  --orchid:#b768aa;
  --amber:#ee9a2c;
}
*{box-sizing:border-box;margin:0;padding:0}
html,body{width:1200px;height:2868px;overflow:hidden;background:var(--white);font-family:'Raleway',sans-serif;color:var(--ink)}
.page{position:relative;width:1200px;height:2868px}
.abs{position:absolute}

/* top bar */
.top-bar{left:0;top:0;width:1200px;height:40px;background:var(--darker);color:var(--white);font:600 13px 'Montserrat',sans-serif}
.top-bar .account{position:absolute;right:30px;top:12px}
.top-bar .account span{font-weight:400;color:#bbb}

/* nav */
.nav{left:0;top:40px;width:1200px;height:64px;background:var(--white)}
.nav a{position:absolute;top:24px;font:600 15px 'Montserrat',sans-serif;color:var(--ink);text-decoration:none}
.pill{background:var(--green);color:var(--white)!important;border-radius:12px;padding:3px 14px;font:600 14px 'Montserrat',sans-serif}
.nav .pill{top:20px}
.cart{position:absolute;left:960px;top:20px;display:flex;gap:6px;align-items:center;font:600 12px 'Montserrat',sans-serif}
.cart .box{border:1px solid #999;padding:4px 8px}

/* hero */
.hero{left:0;top:104px;width:1200px;height:608px;background:linear-gradient(90deg,#6f3277 0%,#a9527f 40%,#d6784f 70%,var(--amber) 100%);text-align:center;color:var(--white)}
.hero h1{position:absolute;left:0;right:0;top:140px;font:400 74px 'Pacifico',cursive;text-shadow:0 2px 8px rgba(0,0,0,.25)}
.hero p{position:absolute;left:0;right:0;top:280px;font:400 24px 'Raleway',sans-serif}
.hero p b{font-weight:700}
.hero .shop-btn{position:absolute;left:548px;top:372px;width:104px;height:40px;background:var(--green);border-radius:20px;font:700 20px/40px 'Montserrat',sans-serif}

/* shop */
.shop{left:0;top:712px;width:1200px;height:588px;background:var(--gray-band)}
.section-title{position:absolute;left:0;right:0;text-align:center;font:700 44px 'Montserrat',sans-serif;color:var(--ink)}
.category{position:absolute;top:188px;width:248px;height:332px}
.category .photo{width:100%;height:100%}
.category .label{position:absolute;left:0;bottom:0;width:100%;height:36px;background:rgba(0,0,0,.65);color:var(--white);text-align:center;font:700 16px/36px 'Montserrat',sans-serif}
.category .label small{font:400 12px 'Raleway',sans-serif;color:#ccc;margin-left:10px}

/* products */
.product{position:absolute;width:232px}
.product .photo{width:232px;height:276px}
.product .name{margin-top:8px;font:400 11px 'Raleway',sans-serif;color:#555}
.product .price{margin-top:6px;font:700 12px 'Montserrat',sans-serif}
.hover-bar{position:absolute;left:0;top:196px;width:232px;height:80px;background:rgba(235,235,235,.9);display:flex;justify-content:space-around;align-items:center;font:600 10px 'Montserrat',sans-serif;text-align:center}
.see-more{left:556px;top:2236px;width:88px;height:34px;border:2px solid var(--ink);font:600 15px/30px 'Montserrat',sans-serif;text-align:center}

/* about */
.rule{height:1px;background:#555}
.about-title{left:0;right:0;top:2348px;text-align:center;font:300 40px 'Raleway',sans-serif}
.about-text{left:300px;width:600px;top:2420px;text-align:center;font:400 14px/20px 'Raleway',sans-serif;color:#444}

/* footer */
.footer{left:0;top:2608px;width:1200px;height:208px;background:var(--dark);color:var(--white)}
.footer h4{position:absolute;top:56px;font:700 13px 'Montserrat',sans-serif;letter-spacing:.5px}
.footer ul{position:absolute;top:80px;list-style:none;font:400 13px/19px 'Raleway',sans-serif;color:#bbb}
.footer .social{position:absolute;top:100px;left:436px;display:flex;gap:18px}
.footer .social span{display:flex;flex-direction:column;align-items:center;gap:4px;font:400 10px 'Raleway',sans-serif;color:#bbb}
.footer .social i{display:block;width:40px;height:40px;border-radius:50%;background:var(--white)}
.footer .pill{position:absolute;left:616px;top:50px}
.footer .contact{position:absolute;left:620px;top:90px;font:400 13px/22px 'Raleway',sans-serif;color:#bbb}
.footer .contact b{color:var(--white);font-weight:600}
.bottom-bar{left:0;top:2816px;width:1200px;height:52px;background:var(--darker);color:#bbb;text-align:center;font:400 13px/52px 'Raleway',sans-serif}
</style>
</head>
<body>
<div class="page">

  <div class="abs top-bar"><div class="account">Sign in <span>or</span> Create an Account</div></div>

  <nav class="abs nav">
    <a style="left:96px">Home</a>
    <a style="left:212px">Products</a>
    <a style="left:352px">About</a>
    <a class="pill" style="left:460px">Contact</a>
    <div class="cart">
      <svg width="26" height="22" viewBox="0 0 26 22"><path d="M1 2h4l3 12h13l3-9H7" fill="none" stroke="#1c1c1c" stroke-width="2"/><circle cx="10" cy="19" r="2" fill="#1c1c1c"/><circle cx="19" cy="19" r="2" fill="#1c1c1c"/></svg>
      <span class="box">0 ITEMS</span><span class="box">$0.00</span>
    </div>
  </nav>

  <header class="abs hero" role="img" aria-label="Wooden desk workspace photo under a purple-to-orange tint">
    <h1>Velvet Harbor</h1>
    <p>We are a company based in <b>NYC</b>, that sells <b>Clothing</b>, <b>Accessories</b> and <b>Electronics</b> on <b>Tradora</b></p>
    <div class="shop-btn">Shop</div>
  </header>

  <section class="abs shop">
    <h2 class="section-title" style="top:72px">Shop</h2>
    <div class="category" style="left:140px">
      <div class="photo" role="img" aria-label="Man in a jacket against a blue wall" style="background:linear-gradient(160deg,#2f64b8,#1c3f7e)"></div>
      <div class="label">Clothing<small>See all</small></div>
    </div>
    <div class="category" style="left:480px">
      <div class="photo" role="img" aria-label="Flat lay of sunglasses, watch and accessories" style="background:linear-gradient(160deg,#5b5550,#2e2a27)"></div>
      <div class="label">Accessories<small>See all</small></div>
    </div>
    <div class="category" style="left:816px">
      <div class="photo" role="img" aria-label="Headphones and gadgets on a desk" style="background:linear-gradient(160deg,#d8d8d8,#7c7c7c)"></div>
      <div class="label">Electronics<small>See all</small></div>
    </div>
  </section>

  <h2 class="section-title" style="top:1380px;font-size:38px">Lastest Products</h2>

  <div class="product" style="left:96px;top:1484px">
    <div class="photo" role="img" aria-label="Man in a coat, street fashion" style="background:linear-gradient(180deg,#6e6a66,#2f2c2a)"></div>
    <div class="hover-bar">
      <div><svg width="28" height="18" viewBox="0 0 28 18"><ellipse cx="14" cy="9" rx="13" ry="8" fill="#1c1c1c"/><circle cx="14" cy="9" r="4" fill="#eee"/></svg><br>View Product</div>
      <div><svg width="26" height="20" viewBox="0 0 26 22"><path d="M1 2h4l3 12h13l3-9H7" fill="none" stroke="#1c1c1c" stroke-width="2.5"/><circle cx="10" cy="19" r="2" fill="#1c1c1c"/><circle cx="19" cy="19" r="2" fill="#1c1c1c"/></svg><br>Add To Cart</div>
    </div>
    <div class="name">Lorem ipsum cotton tee</div><div class="price">$00.99</div>
  </div>
  <div class="product" style="left:356px;top:1484px">
    <div class="photo" role="img" aria-label="Denim shirt detail" style="background:linear-gradient(180deg,#6b88ac,#3b5576)"></div>
    <div class="name">Lorem ipsum denim shirt</div><div class="price">$00.99</div>
  </div>
  <div class="product" style="left:612px;top:1484px">
    <div class="photo" role="img" aria-label="Person in a blue sweater seen from behind" style="background:linear-gradient(180deg,#e7d9c4,#4f6a92)"></div>
    <div class="name">Lorem ipsum knit sweater</div><div class="price">$00.99</div>
  </div>
  <div class="product" style="left:872px;top:1484px">
    <div class="photo" role="img" aria-label="Laptop on a desk" style="background:linear-gradient(180deg,#b9c7d6,#3d5f8a)"></div>
    <div class="name">Lorem ipsum slim laptop</div><div class="price">$00.99</div>
  </div>

  <div class="product" style="left:96px;top:1852px">
    <div class="photo" role="img" aria-label="Man in a navy suit and tie" style="background:linear-gradient(180deg,#3b4664,#141a2b)"></div>
    <div class="name">Lorem ipsum tailored suit</div><div class="price">$00.99</div>
  </div>
  <div class="product" style="left:356px;top:1852px">
    <div class="photo" role="img" aria-label="Grey t-shirt on a person" style="background:linear-gradient(180deg,#6a625b,#3b3632)"></div>
    <div class="name">Lorem ipsum grey tee</div><div class="price">$00.99</div>
  </div>
  <div class="product" style="left:612px;top:1852px">
    <div class="photo" role="img" aria-label="Orange phone and earbuds on a table" style="background:linear-gradient(180deg,#8d8a86,#c5702a)"></div>
    <div class="name">Lorem ipsum phone case</div><div class="price">$00.99</div>
  </div>
  <div class="product" style="left:872px;top:1852px">
    <div class="photo" role="img" aria-label="Woman in a plaid shirt" style="background:linear-gradient(180deg,#cfd7da,#b5475a)"></div>
    <div class="name">Lorem ipsum plaid shirt</div><div class="price">$00.99</div>
  </div>

  <div class="abs see-more">See More</div>

  <div class="abs rule" style="left:220px;top:2372px;width:250px"></div>
  <div class="abs rule" style="left:730px;top:2372px;width:250px"></div>
  <h2 class="abs about-title">About Us</h2>
  <p class="abs about-text">Lorem ipsum dolor sit amet, consectetur adipiscing elit. Maecenas non ornare arcu. Phasellus elementum mauris at dolor ultrices lobortis. Nunc semper quam ac turpis facilisis posuere. Duis eget porttitor metus.</p>
  <div class="abs rule" style="left:96px;top:2544px;width:1008px"></div>

  <footer class="abs footer">
    <h4 style="left:148px">QUESTIONS?</h4>
    <ul style="left:148px"><li>FAQs</li><li>Track Order</li><li>Returns</li></ul>
    <h4 style="left:292px">MENU</h4>
    <ul style="left:292px"><li>Home</li><li>Products</li><li>About</li><li>Contact</li></ul>
    <h4 style="left:416px">FIND US ON SOCIAL MEDIA</h4>
    <div class="social"><span><i></i>Chirper</span><span><i></i>Friendbook</span></div>
    <span class="pill">Contact</span>
    <div class="contact">Email: <b>hello@velvetharbor-mail.com</b><br>Call Us: <b>(212) 555-0147</b></div>
  </footer>
  <div class="abs bottom-bar">&copy;2015 Velvet Harbor LLC</div>

</div>
</body>
</html>
```